Poster Design Project- kids dancing/sport

I need a poster design for a childrens dance and sport program!!
I have attached a brochure and logo designs. From the brochure please include information from sections titled "twirl'n'hop" and "themes". Also please put on the phone number and email address (found on the brochure). Emphasis on FUN!! Make poster colourful, very kid friendly and eye catching.
Some other things i would like on the poster are:
"Does your child love to dance, sing and play sport?? Why not enrol them in our fun-filled program?"
"From only $10.00 per class"
"Sign up for your FREE trial class today"
"A fun introduction to the joy of Dance, Sport and Music for 2-6yr olds. Held in your childcare centre!!"
Hi!!
I would like to stress its TRIAL class not TRAIL class. Please feel free to play around with the information, it doesnt need to be in one blurb. Also i have updated the brief. I would like "Does you child love to dance, sing or play sport? Why not enrol in our fun filled program?" or something to that effect!!
Thanks!!!!
2-6yr olds and their parents
Childcare

```html
<!DOCTYPE html>
<html lang="en">
<head>
<meta charset="utf-8">
<title>Twirl 'n' Hop</title>
<link rel="stylesheet" href="https://fonts.googleapis.com/css2?family=Source+Sans+3:wght@400;600&family=Short+Stack&family=Questrial&family=Titan+One&display=swap">
<style>
  :root {
    --stripe-red: #e0344f;
    --stripe-yellow: #f6e08e;
    --stripe-green: #a3d07a;
    --stripe-blue: #87d0ec;
    --stripe-purple: #5a4fa0;
    --ink: #000000;
    --pink: #e8327e;
    --cream: #f6e58f;
    --sky: #8fd3ee;
    --lime: #b5d882;
    --white: #ffffff;
  }
  html, body { margin: 0; padding: 0; overflow: hidden; background: var(--ink); }
  .poster {
    position: relative;
    width: 826px;
    height: 1200px;
    overflow: hidden;
    background: var(--ink);
    font-family: "Source Sans 3", sans-serif;
    color: var(--white);
  }
  .rainbow { position: absolute; left: 0; top: 0; width: 826px; height: 507px; display: flex; }
  .rainbow span { flex: 1; }
  .rainbow .red { background: var(--stripe-red); }
  .rainbow .yellow { background: var(--stripe-yellow); }
  .rainbow .green { background: var(--stripe-green); }
  .rainbow .blue { background: var(--stripe-blue); }
  .rainbow .purple { background: var(--stripe-purple); }

  .headline {
    position: absolute; left: 0; top: 62px; width: 826px; margin: 0;
    text-align: center;
    font-family: "Titan One", sans-serif;
    font-weight: 400;
    font-size: 86px; line-height: 1;
    color: var(--ink);
    letter-spacing: 1px;
  }
  .dancers-art {
    position: absolute; left: 12px; top: 198px; width: 808px; height: 309px;
    background: linear-gradient(to bottom, rgba(0,0,0,0) 0%, rgba(0,0,0,0.55) 40%, rgba(0,0,0,0.85) 100%);
    border-radius: 120px 120px 0 0;
  }
  .program-name {
    position: absolute; left: 0; top: 516px; width: 826px; margin: 0;
    text-align: center;
    font-family: "Titan One", sans-serif; font-weight: 400;
    font-size: 34px; line-height: 1; color: var(--pink);
  }
  .tagline {
    position: absolute; left: 0; top: 563px; width: 826px; margin: 0;
    text-align: center;
    font-family: "Short Stack", cursive;
    font-size: 22px; line-height: 30px; color: var(--cream);
  }
  .offer {
    position: absolute; left: 0; top: 640px; width: 826px; margin: 0;
    text-align: center; font-size: 21px; line-height: 28px;
  }
  .offer .accent { color: var(--pink); }
  .offer .price { font-size: 34px; color: var(--white); vertical-align: -2px; }
  .contact {
    position: absolute; left: 0; top: 720px; width: 826px; margin: 0;
    text-align: center; font-size: 18px; line-height: 24px;
  }
  .contact .accent { color: var(--pink); }
  .kids-art {
    position: absolute; left: 153px; top: 768px; width: 530px; height: 120px;
    background: linear-gradient(90deg, #e9675a, #f3d56b, #d43a8a, #5fb04d, #39a3b5, #e4405f, #f2c12e);
    opacity: 0.75; border-radius: 60px;
  }
  .intro-band {
    position: absolute; left: 27px; top: 893px; width: 777px; height: 37px;
    background: var(--pink);
    display: flex; align-items: center; justify-content: center;
    font-size: 15.5px; color: var(--white); margin: 0;
  }
  .themes-title {
    position: absolute; left: 0; top: 950px; width: 826px; margin: 0;
    text-align: center;
    font-family: "Questrial", sans-serif; font-weight: 400;
    font-size: 44px; line-height: 52px; color: var(--pink);
  }
  .rule { position: absolute; top: 982px; height: 1px; background: var(--white); }
  .rule.left { left: 43px; width: 276px; }
  .rule.right { left: 536px; width: 261px; }
  .theme-list {
    position: absolute; top: 1012px; margin: 0; padding: 0; list-style: none;
    font-size: 16.5px; line-height: 21.2px;
  }
  .theme-list li { position: relative; padding-left: 22px; white-space: nowrap; }
  .theme-list svg { position: absolute; left: 0; top: 5px; width: 12px; height: 11px; fill: var(--pink); }
  .col-one { left: 33px; color: var(--cream); }
  .col-two { left: 267px; color: var(--sky); top: 1010px; }
  .col-three { left: 612px; color: var(--lime); }
</style>
</head>
<body>
<svg width="0" height="0" style="position:absolute">
  <symbol id="heart" viewBox="0 0 24 22"><path d="M12 21.5 2.6 12.3C-.6 9.1-.6 4.2 2.6 1.6 5.4-.6 9.4.1 12 3.2 14.6.1 18.6-.6 21.4 1.6c3.2 2.6 3.2 7.5 0 10.7Z"/></symbol>
</svg>
<main class="poster">
  <div class="rainbow" aria-hidden="true">
    <span class="red"></span><span class="yellow"></span><span class="green"></span><span class="blue"></span><span class="purple"></span>
  </div>
  <h1 class="headline">TWIRL 'N' HOP</h1>
  <div class="dancers-art" role="img" aria-label="Silhouettes of five children dancing and singing with music notes"></div>

  <h2 class="program-name">TWIRL 'N' HOP</h2>
  <p class="tagline">Does your child love to dance, sing and play sport??<br>Why not enrol them in our fun-filled program?</p>
  <p class="offer">
    <span class="accent">From only</span> <span class="price">$10.00</span> <span class="accent">per class</span><br>
    <span class="accent">Sign up for your</span> FREE trial class today
  </p>
  <p class="contact"><span class="accent">Contact</span> : Phone: 0400 218 765 | &nbsp;Email: twirlnhop@example.com</p>

  <div class="kids-art" role="img" aria-label="Colourful cartoon children holding hands and dancing in a row"></div>
  <p class="intro-band">"A fun introduction to the joy of Dance, Sport and Music for 2-6yr olds. Held in your childcare centre!!"</p>

  <h2 class="themes-title">Themes</h2>
  <div class="rule left"></div>
  <div class="rule right"></div>

  <ul class="theme-list col-one">
    <li><svg><use href="#heart"/></svg>Jumping Jellybeans</li>
    <li><svg><use href="#heart"/></svg>Under the Sea</li>
    <li><svg><use href="#heart"/></svg>Superheros</li>
    <li><svg><use href="#heart"/></svg>Jungle Jam</li>
    <li><svg><use href="#heart"/></svg>Movie Magic</li>
    <li><svg><use href="#heart"/></svg>Balancing Bugs</li>
    <li><svg><use href="#heart"/></svg>Mexican Fiesta</li>
  </ul>
  <ul class="theme-list col-two">
    <li><svg><use href="#heart"/></svg>Gymnastics and Rhythmic Gymnastics</li>
    <li><svg><use href="#heart"/></svg>Disco Divas and Singing Superstars</li>
    <li><svg><use href="#heart"/></svg>Hawaiian Holiday</li>
    <li><svg><use href="#heart"/></svg>Circus</li>
    <li><svg><use href="#heart"/></svg>Space</li>
    <li><svg><use href="#heart"/></svg>Bowling and Ball Skills</li>
    <li><svg><use href="#heart"/></svg>Colours and Shapes</li>
  </ul>
  <ul class="theme-list col-three">
    <li><svg><use href="#heart"/></svg>Monsters</li>
    <li><svg><use href="#heart"/></svg>Magical Fairytales</li>
    <li><svg><use href="#heart"/></svg>Sport and Cheerleading</li>
    <li><svg><use href="#heart"/></svg>Mexican Fiesta</li>
    <li><svg><use href="#heart"/></svg>Animals</li>
    <li><svg><use href="#heart"/></svg>Aboriginal Adventure</li>
    <li><svg><use href="#heart"/></svg>Its Party Time</li>
  </ul>
</main>
</body>
</html>
```